High-end residential home builder needs a business card design

We need a new business card design for a small residential construction company based in Boise, Idaho. We specialize in building custom high-end homes and remodels, with a focus on great design and craftsmanship.

We would like to use our current logo, but open to new color suggestions.
Just looking for a clean, sharp, modern design that looks high-end.

Target Market(s)

Upscale clientele

Industry/Entity Type

Contractor

Contact Information for Business Card

Company: Stonefield Custom Builders
Name: Marcus Tilley
Phone number: 208 367 4120
Email: MarcusTilleySCB@mailbox-example.com
Website: Stonefieldcustombuilders-example.com

Font styles to use
Serif
Sans Serif

Requirements
Must have
• Company Logo
Company name
My name
My phone number
My email
Company website
Nice to have
• I have attached a few photos of cards that I really like.

```html
<!DOCTYPE html>
<html lang="en">
<head>
<meta charset="utf-8">
<title>Stonefield Custom Builders – Business Card</title>
<link rel="stylesheet" href="https://fonts.googleapis.com/css2?family=Montserrat:wght@300;400;600;700&family=Open+Sans:wght@400;700&display=swap">
<style>
  :root {
    --bg: #e4e5e7;
    --brown: #2f1d12;
    --brown-light: #45291a;
    --brown-mark: #5a3a27;
    --orange: #e8921e;
    --white: #ffffff;
    --ink: #1e1612;
  }
  * { margin: 0; padding: 0; box-sizing: border-box; }
  html, body { width: 1200px; height: 800px; overflow: hidden; }
  body {
    background: var(--bg);
    position: relative;
    font-family: "Open Sans", sans-serif;
  }
  .card {
    position: absolute;
    box-shadow: 0 6px 18px rgba(0,0,0,0.18);
    overflow: hidden;
  }

  /* Front */
  .card-front {
    left: 150px; top: 110px;
    width: 340px; height: 580px;
    background: var(--white);
  }
  .front-band { position: absolute; left: 0; top: 0; }
  .wordmark {
    position: absolute; left: 0; right: 0; top: 196px;
    display: flex; align-items: center; justify-content: center; gap: 10px;
  }
  .wordmark-square {
    width: 16px; height: 16px; background: var(--orange);
  }
  .wordmark-name {
    font-family: "Montserrat", sans-serif;
    font-weight: 700; font-size: 26px; line-height: 1; color: var(--brown);
  }
  .company {
    position: absolute; left: 0; right: 0; top: 252px;
    text-align: center;
  }
  .company-name {
    font-family: "Montserrat", sans-serif; font-weight: 600;
    font-size: 21px; letter-spacing: 6px; color: var(--brown);
    padding: 0 0 6px 6px;
    border-bottom: 1.5px solid var(--brown);
    display: inline-block;
  }
  .company-tag {
    font-family: "Montserrat", sans-serif; font-weight: 400;
    font-size: 12.5px; letter-spacing: 4.5px; color: var(--orange);
    padding-left: 4.5px;
    margin-top: 6px;
  }
  .person {
    position: absolute; left: 0; right: 0; top: 345px;
    text-align: center;
  }
  .person-name {
    font-family: "Montserrat", sans-serif; font-weight: 700;
    font-size: 17px; color: var(--ink);
  }
  .person-role {
    font-family: "Montserrat", sans-serif; font-weight: 400;
    font-size: 13px; color: var(--orange); margin-top: 2px;
  }
  .contact-divider {
    position: absolute; left: 40px; top: 420px;
  }
  .contact {
    position: absolute; left: 0; right: 0; top: 450px;
    text-align: center; color: var(--ink);
    font-size: 12.5px; line-height: 1.55;
  }
  .contact-web { font-weight: 700; font-size: 13px; }

  /* Back */
  .card-back {
    left: 560px; top: 230px;
    width: 580px; height: 340px;
    background: linear-gradient(135deg, var(--brown-light), var(--brown) 60%);
    display: flex; align-items: center; justify-content: center;
  }
  .back-mark {
    font-family: "Montserrat", sans-serif; font-weight: 700;
    font-size: 34px; color: var(--brown-mark);
  }
</style>
</head>
<body>

  <section class="card card-front" aria-label="Business card front">
    <svg class="front-band" width="340" height="580" viewBox="0 0 340 580" aria-hidden="true">
      <polygon points="0,0 340,0 340,55 255,55 230,110 0,175" fill="var(--brown)"/>
    </svg>

    <div class="wordmark">
      <span class="wordmark-square"></span>
      <span class="wordmark-name">Stonefield</span>
    </div>

    <div class="company">
      <div class="company-name">STONEFIELD</div>
      <div class="company-tag">CUSTOM BUILDERS</div>
    </div>

    <div class="person">
      <div class="person-name">MARCUS TILLEY</div>
      <div class="person-role">FOUNDER</div>
    </div>

    <svg class="contact-divider" width="260" height="24" viewBox="0 0 260 24" aria-hidden="true">
      <line x1="0" y1="12" x2="260" y2="12" stroke="var(--orange)" stroke-width="1.5"/>
      <circle cx="106" cy="12" r="9" fill="var(--orange)"/>
      <circle cx="130" cy="12" r="9" fill="var(--orange)"/>
      <circle cx="154" cy="12" r="9" fill="var(--orange)"/>
      <path d="M102.5 8 q1-1 2 0 l1 2 q-1 1 0 2 l1 1 q1 1 2 0 l2 1 q1 1 0 2 q-3 2-6-1 q-3-3-2-7z" fill="var(--white)"/>
      <rect x="125" y="8" width="10" height="8" fill="none" stroke="var(--white)" stroke-width="1.2"/>
      <polyline points="125,8 130,12.5 135,8" fill="none" stroke="var(--white)" stroke-width="1.2"/>
      <circle cx="154" cy="12" r="5" fill="none" stroke="var(--white)" stroke-width="1.2"/>
      <line x1="149" y1="12" x2="159" y2="12" stroke="var(--white)" stroke-width="1"/>
      <ellipse cx="154" cy="12" rx="2.2" ry="5" fill="none" stroke="var(--white)" stroke-width="1"/>
    </svg>

    <div class="contact">
      <div class="contact-phone">208 367 4120</div>
      <div class="contact-email">MarcusTilleySCB@mailbox-example.com</div>
      <div class="contact-web">Stonefieldcustombuilders-example.com</div>
    </div>
  </section>

  <section class="card card-back" aria-label="Business card back">
    <span class="back-mark">Stonefield</span>
  </section>

</body>
</html>
```